I need a business Card Design for my practice , i am clinical herbalist. I am a herbalist specializing in Lyme disease, autism, autoimmune diseases, difficult to cure diseasesDifficult to cure diseases. In my innovative practice i link traditional medicine, herbs with science, immunologu ,pharmacology.

Industry/Entity Type

Business

Contact Information for Business Card

My company name : OSRODEK ZIELNIKA
My name : Piotr Weltak
Name of my profession : Fitoterapeuta
In Polish language Fitoterapeuta is Herbalist .

e-mail: piotrweltak@osrodekzielnika.com
www.osrodek-zielnika.pl
phone : 574 806 215
My company adress : Dąbrowa Sękowska 14 , 38-415 Mielnik
I dont have logo .

Requirements
Nice to have
• My company

```html
<!DOCTYPE html>
<html lang="pl">
<head>
<meta charset="UTF-8">
<title>Ośrodek Zielnika – wizytówka</title>
<link rel="stylesheet" href="https://fonts.googleapis.com/css2?family=Arimo:wght@400;700&family=Oswald:wght@600&display=swap">
<style>
  :root {
    --page-bg: #e6e6e4;
    --card-white: #ffffff;
    --brand-blue: #0683b4;
    --brand-deep: #0a5878;
    --brand-band: #045275;
    --ink: #111111;
    --on-blue: #ffffff;
  }
  * { margin: 0; padding: 0; box-sizing: border-box; }
  html, body {
    width: 1200px; height: 1135px; overflow: hidden;
    background: var(--page-bg);
    font-family: "Arimo", Arial, sans-serif;
  }
  .card {
    position: absolute;
    width: 680px; height: 406px;
    overflow: hidden;
    box-shadow: 0 6px 18px rgba(0,0,0,0.18);
  }
  /* FRONT */
  .card--front { left: 235px; top: 90px; background: var(--card-white); }
  .front__panel {
    position: absolute; left: 359px; top: 0; right: 0; bottom: 0;
    background: var(--brand-blue);
  }
  .front__tab {
    position: absolute; left: 334px; top: 101px;
    width: 30px; height: 285px;
    background: var(--brand-blue);
  }
  .front__rail {
    position: absolute; left: 292px; top: 122px;
    width: 67px; height: 243px;
    background: var(--brand-deep);
  }
  .front__company {
    position: absolute; left: 0; width: 292px; top: 152px;
    text-align: center;
    font-size: 35px; line-height: 39px;
    color: var(--ink); letter-spacing: 0.5px;
  }
  .front__name {
    position: absolute; left: 367px; top: 44px;
    font-family: "Oswald", "Arial Narrow", sans-serif;
    font-weight: 600; font-size: 28px; line-height: 34px;
    color: var(--on-blue);
  }
  .front__role {
    position: absolute; left: 367px; top: 80px;
    font-size: 16px; color: var(--on-blue);
  }
  .contact {
    position: absolute; left: 316px;
    display: flex; align-items: center;
    color: var(--on-blue); font-size: 17px;
  }
  .contact svg { width: 24px; height: 24px; margin-right: 27px; flex: none; }
  .contact--phone { top: 176px; }
  .contact--mail  { top: 238px; }
  .contact--web   { top: 300px; }
  /* BACK */
  .card--back { left: 239px; top: 625px; background: var(--brand-blue); }
  .back__company {
    position: absolute; left: 0; right: 0; top: 108px;
    text-align: center;
    font-size: 73px; line-height: 76px;
    color: var(--on-blue); letter-spacing: 1px;
  }
  .back__band {
    position: absolute; left: 0; right: 0; top: 282px; height: 43px;
    background: var(--brand-band);
  }
</style>
</head>
<body>

<section class="card card--front">
  <div class="front__panel"></div>
  <div class="front__tab"></div>
  <div class="front__rail"></div>

  <h1 class="front__company">OSRODEK<br>ZIELNIKA</h1>

  <p class="front__name">Piotr Weltak</p>
  <p class="front__role">Fitoterapeuta</p>

  <p class="contact contact--phone">
    <svg viewBox="0 0 24 24" aria-hidden="true"><path fill="#fff" d="M6.6 2.5c.6-.3 1.3-.1 1.6.5l1.7 3.4c.3.6.1 1.2-.4 1.6l-1.4 1c.7 2.2 2 4.3 3.8 6l1.3-1.1c.5-.4 1.2-.4 1.7 0l2.9 2.4c.5.4.6 1.1.2 1.7l-1.3 1.9c-.5.7-1.4 1-2.2.7C9.2 18.8 5.3 13.9 4.4 7.7c-.1-.9.3-1.7 1-2.1z"/></svg>
    574 806 215
  </p>
  <p class="contact contact--mail">
    <svg viewBox="0 0 24 24" aria-hidden="true" fill="none" stroke="#fff" stroke-width="1.6"><circle cx="12" cy="12" r="9.5"/><ellipse cx="12" cy="12" rx="4.2" ry="9.5"/><line x1="2.5" y1="12" x2="21.5" y2="12"/><path d="M4.3 7h15.4M4.3 17h15.4"/></svg>
    piotrweltak@osrodekzielnika.com
  </p>
  <p class="contact contact--web">
    <svg viewBox="0 0 24 24" aria-hidden="true"><path fill="#fff" fill-rule="evenodd" d="M12 1.5a7 7 0 0 1 7 7c0 5-7 14-7 14s-7-9-7-14a7 7 0 0 1 7-7zm0 4a3 3 0 1 0 0 6 3 3 0 0 0 0-6z"/></svg>
    www.osrodek-zielnika.pl
  </p>
</section>

<section class="card card--back">
  <h2 class="back__company">OSRODEK<br>ZIELNIKA</h2>
  <div class="back__band"></div>
</section>

</body>
</html>
```